Redesign of outdated "Automotive Automation Company"

We are looking to finally update our outdated website with some cutting edge graphics. We want our customers to know we value technology and are cutting edge as far as design. We provide automation solutions for the automotive industry which essentially means we program robots, and sell automation related products.

Current URL

http://lnk.vemrota.com/Qx7pwe
Updates

Project Deadline Extended
Reason: The client portal wasn't working, it's just finally been fixed by Pixel Harbor. I will go through and start reviewing designs.

We are trying to go with the same look and feel on our business cards, line cards, apparel, etc. so we are forming a brand. I have included the current draft of the line card. Please utilize our newest Logo TLV Standardized Logo.jpg http://img.solvarenpics.com/pz3Tm8d.jpg?1 Also we are trying hard to sell the following software / hardware companies so we can put some emphasis on their product. Meridel Controls https://www.meridelcontrols.com/ We make money on selling the software and then on the integration. I think you should tie in this animation. ยท From Shop Chaos to Smooth Output https://media.vorplexclips.com/deliveries/938127a4b51dfe03c7724bde1209f74a615b830c.jpg?image_play_button=true&image_play_button_color=7b796ae0&image_crop_resized=275x155 In this 2-minute video, discover how Quellwave can help run your plant floor. We are Authorized Integrators / Resellers for Tamberly Mechatronics Varnoth Sensorik http://varnoth.com/en/usa/ Meridel Controls https://www.meridelcontrols.com/ Corvane Process Works www.cpwkx.com Halberd Transfer Corp www.halberdtransfer.com Pennwick Machining http://www.pennwickmachining.com/strategic_partners.aspx

Target Market(s)

Large automotive companies looking for automation or robotic programming. So Professional is key.

Industry/Entity Type

Automotive

Font styles to use
Other font styles liked:
• Possible Open Sans or Lato

Colors
0591cc
ceeaf6
fbd4d5
fbf289
fece3e

Requirements
Must have
• Professional Modern Design.

I want a homepage design, and a rough Sales Page... Where numerous products can be listed.
Nice to have
• Maybe an updated logo if possible.

```html
<!DOCTYPE html>
<html lang="en">
<head>
<meta charset="utf-8">
<title>TLV Engineering Solutions</title>
<link href="https://fonts.googleapis.com/css2?family=Open+Sans:wght@400;600;700;800&family=Lato:wght@400;700&display=swap" rel="stylesheet">
<style>
:root{
  --black:#000;
  --white:#fff;
  --green:#1fa82c;
  --green-bright:#27e03a;
  --green-text:#2f9e2a;
  --grey-nav:#e6e6e6;
  --grey-line:#7a7a7a;
  --text:#111;
  --social:#5a5a5a;
}
*{margin:0;padding:0;box-sizing:border-box}
html,body{width:1200px;height:1000px;overflow:hidden;background:var(--white)}
body{position:relative;font-family:'Open Sans',sans-serif;color:var(--text)}
.site-header{position:absolute;left:0;top:0;width:1200px;height:100px;background:var(--black)}
.brand{position:absolute;left:158px;top:24px;color:var(--white);display:flex;align-items:baseline;gap:16px}
.brand-name{font-family:'Lato',sans-serif;font-weight:700;font-size:40px;letter-spacing:-1px}
.brand-tag{font-weight:700;font-size:14px}
.social{position:absolute;left:830px;top:12px;width:155px;text-align:center}
.social-label{color:var(--green);font-size:15px;display:block}
.social-icons{display:flex;gap:7px;justify-content:center;margin-top:4px}
.social-icons span{width:32px;height:32px;border-radius:50%;background:var(--social);display:block}
.hero{position:absolute;left:0;top:0;width:1200px;height:570px}
.main-nav{position:absolute;left:162px;top:81px;width:875px;height:40px;background:var(--grey-nav);border-radius:20px;display:flex;align-items:center;overflow:hidden;font-family:'Lato',sans-serif;font-size:20px}
.nav-item{height:40px;display:flex;align-items:center;justify-content:center;gap:8px;border-right:2px solid #fff;color:#111}
.nav-item svg{width:24px;height:22px}
.nav-home{width:124px;background:linear-gradient(#5aff63,#15c51f);color:var(--white);border-radius:20px 0 0 20px}
.nav-services{width:150px}
.nav-contact{width:150px}
.nav-about{width:150px}
.search{margin-left:8px;width:275px;height:24px;background:var(--white);display:flex;align-items:center;justify-content:space-between;padding:0 8px 0 14px;font-size:18px}
.search svg{width:20px;height:20px}
.slider-arrow{position:absolute;top:228px;width:35px;height:70px;background:rgba(200,200,200,.85)}
.slider-arrow.prev{left:15px}
.slider-arrow.next{left:1145px}
.cta-band{position:absolute;left:0;top:332px;width:493px;height:71px;background:rgba(40,40,40,.7);color:var(--white);text-align:right;padding-right:8px}
.cta-title{font-weight:700;font-size:33px;line-height:44px;padding-right:20px;text-shadow:2px 2px 3px #000}
.cta-sub{font-weight:700;font-size:15px;line-height:18px;text-shadow:1px 1px 2px #000}
.welcome-band{position:absolute;left:621px;top:332px;width:579px;height:71px;background:rgba(31,168,44,.72);color:var(--white);padding-left:2px;text-shadow:2px 2px 3px #000}
.welcome-small{font-weight:700;font-size:19px;line-height:24px;padding-top:5px}
.welcome-large{font-weight:700;font-size:33px;line-height:36px}
.intro{position:absolute;left:120px;top:619px;width:960px;height:273px;border-top:2px solid var(--grey-line);border-bottom:2px solid var(--grey-line);text-align:center}
.intro-title{color:var(--green-text);font-weight:800;font-size:31px;margin-top:25px;line-height:40px;text-shadow:1px 1px 2px rgba(0,0,0,.3)}
.intro-sub{font-family:'Lato',sans-serif;font-weight:700;font-size:30px;line-height:40px;margin-top:11px;text-shadow:1px 1px 2px rgba(0,0,0,.25)}
.intro-text{font-size:16px;line-height:36px;width:820px;margin:0 auto;margin-top:0}
.services{position:absolute;left:120px;top:924px;width:960px;height:76px;background:linear-gradient(90deg,#0b0d0d,#3a4a3e 35%,#2e3f33 60%,#121414);text-align:center}
.services-title{font-family:'Lato',sans-serif;font-weight:700;font-size:50px;color:var(--white);text-decoration:underline;text-decoration-thickness:3px;text-underline-offset:6px;line-height:92px}
</style>
</head>
<body>
<svg class="hero" viewBox="0 0 1200 570" role="img" aria-label="Futuristic robotic assembly platform with green robot arms">
  <defs>
    <linearGradient id="heroFill" x1="0" y1="0" x2="1" y2="1">
      <stop offset="0" stop-color="#1b2226"/>
      <stop offset=".35" stop-color="#6f8a2a"/>
      <stop offset=".55" stop-color="#b8bcbf"/>
      <stop offset=".75" stop-color="#5f7a26"/>
      <stop offset="1" stop-color="#1a2024"/>
    </linearGradient>
  </defs>
  <polygon points="0,100 1200,100 1200,525 300,565 0,490" fill="url(#heroFill)"/>
  <polygon points="0,410 300,520 1200,430 1200,525 300,565 0,490" fill="#000"/>
  <polygon points="0,440 300,552 1200,488 1200,515 300,566 0,468" fill="#1fa82c"/>
</svg>

<header class="site-header">
  <div class="brand"><span class="brand-name">LOGO</span><span class="brand-tag">Engineering Solutions!</span></div>
  <div class="social">
    <span class="social-label">Join The Conversation</span>
    <div class="social-icons"><span aria-label="Social link"></span><span aria-label="Social link"></span><span aria-label="Social link"></span><span aria-label="Social link"></span></div>
  </div>
</header>

<nav class="main-nav">
  <div class="nav-item nav-home">
    <svg viewBox="0 0 24 22"><path d="M12 2 1 12h3v9h6v-6h4v6h6v-9h3z" fill="#fff"/></svg>Home
  </div>
  <div class="nav-item nav-services">
    <svg viewBox="0 0 24 22" fill="#222"><rect x="1" y="1" width="6" height="5"/><rect x="9" y="1" width="6" height="5"/><rect x="17" y="1" width="6" height="5"/><rect x="1" y="8.5" width="6" height="5"/><rect x="9" y="8.5" width="6" height="5"/><rect x="17" y="8.5" width="6" height="5"/><rect x="1" y="16" width="6" height="5"/><rect x="9" y="16" width="6" height="5"/><rect x="17" y="16" width="6" height="5"/></svg>Services
  </div>
  <div class="nav-item nav-contact">
    <svg viewBox="0 0 30 22" style="width:30px"><rect x="1" y="3" width="28" height="17" fill="#111"/><path d="M1 3 15 13 29 3" stroke="#e6e6e6" stroke-width="2" fill="none"/></svg>Contact
  </div>
  <div class="nav-item nav-about">
    <svg viewBox="0 0 24 22" fill="#111"><circle cx="9" cy="6" r="5"/><path d="M0 21c0-6 4-9 9-9s9 3 9 9z"/><circle cx="16" cy="5" r="4"/><path d="M14 11c5 0 10 2 10 8h-5c0-3-2-6-5-8z"/></svg>About
  </div>
  <div class="search">Search
    <svg viewBox="0 0 20 20"><circle cx="8" cy="8" r="6" stroke="#111" stroke-width="2.5" fill="none"/><path d="M12.5 12.5 18 18" stroke="#111" stroke-width="3"/></svg>
  </div>
</nav>

<div class="slider-arrow prev"><svg viewBox="0 0 35 70" width="35" height="70"><path d="M26 12 8 35l18 23" stroke="#1fa82c" stroke-width="8" fill="none"/></svg></div>
<div class="slider-arrow next"><svg viewBox="0 0 35 70" width="35" height="70"><path d="M9 12l18 23-18 23" stroke="#1fa82c" stroke-width="8" fill="none"/></svg></div>

<div class="cta-band">
  <div class="cta-title">Learn More &gt;&gt;&gt;</div>
  <div class="cta-sub">Find out how we can help your business!</div>
</div>
<div class="welcome-band">
  <div class="welcome-small">Welcome to the</div>
  <div class="welcome-large">TLV Engineering Solutions!</div>
</div>

<section class="intro">
  <h1 class="intro-title">Welcome to TLV Engineering Solutions Inc!</h1>
  <h2 class="intro-sub">Your Premier Automation Consulting &amp; Systems Integration choice!</h2>
  <p class="intro-text">Industrial Automation is constantly evolving with ever-changing technological breakthroughs. For companies to remain competitive, they need to be more nimble than ever implementing productivity and manufacturing innovations. But identifying and implementing the right Automation, Robotics and industrial Controls is never easy. That's where our team of experts comes in to play bringing our proven experience to the table.</p>
</section>

<section class="services" role="img" aria-label="Blurred industrial machinery background">
  <h2 class="services-title">Our Services!</h2>
</section>
</body>
</html>
```